Business Card for Business consulting practice

Need a design for a consultant business card. Simple and elegant.
I need the following information on the card:
Logo: (see uploaded file)
Company name: Calmora Advisory Group
Name: Dana Weltrup
Title: Managing Director - Aerospace and Defence
Phone #: 514-268-3917
e-mail: dana.weltrup@calmora-example.com
Website: www.calmora-example.com
Tagline: Proposals Management and Capture support for complex procurements

```html
<!DOCTYPE html>
<html lang="en">
<head>
<meta charset="utf-8">
<title>Calmora Advisory Group – Business Card</title>
<link href="https://fonts.googleapis.com/css2?family=Raleway:wght@400;500;700&display=swap" rel="stylesheet">
<style>
  :root {
    --navy: #0d2c40;
    --navy-deep: #0a2334;
    --accent: #2a9bc4;
    --accent-bright: #35b3ea;
    --white: #ffffff;
    --page: #e4e7ea;
  }
  * { box-sizing: border-box; margin: 0; padding: 0; }
  html, body { width: 1200px; height: 912px; overflow: hidden; }
  body {
    background: var(--page);
    font-family: "Raleway", Arial, sans-serif;
    position: relative;
  }
  .card {
    position: absolute;
    left: 250px;
    width: 700px;
    height: 400px;
    background: var(--navy);
    overflow: hidden;
    box-shadow: 0 6px 18px rgba(0,0,0,0.18);
  }
  .card--back { top: 36px; }
  .card--front { top: 476px; }

  .back-pattern {
    position: absolute;
    inset: 0;
    background: linear-gradient(35deg, var(--navy-deep) 0%, var(--navy) 40%, #135a82 70%, var(--accent-bright) 100%);
  }

  .brand {
    position: absolute;
    top: 86px;
    left: 0;
    width: 100%;
    display: flex;
    justify-content: center;
    align-items: center;
    gap: 14px;
  }
  .brand__dot {
    width: 22px; height: 22px;
    border-radius: 50%;
    background: var(--accent);
  }
  .brand__name {
    color: var(--white);
    font-weight: 500;
    font-size: 32px;
    letter-spacing: 2px;
    text-transform: uppercase;
  }
  .brand__rule {
    position: absolute;
    top: 140px;
    left: 140px;
    width: 420px;
    height: 2px;
    background: var(--accent);
  }

  .person {
    position: absolute;
    top: 196px;
    right: 370px;
    text-align: right;
    color: var(--white);
  }
  .person__name {
    color: var(--accent);
    font-weight: 700;
    font-size: 24px;
    letter-spacing: 0.5px;
    text-transform: uppercase;
    margin-bottom: 4px;
  }
  .person__role { font-size: 16px; line-height: 1.3; }

  .divider {
    position: absolute;
    top: 190px;
    left: 348px;
    width: 2px;
    height: 86px;
    background: var(--accent);
  }

  .contact {
    position: absolute;
    top: 196px;
    left: 366px;
    list-style: none;
    color: var(--white);
    font-size: 15px;
  }
  .contact li {
    display: flex;
    align-items: center;
    gap: 8px;
    height: 24px;
  }
  .contact svg { width: 13px; height: 13px; flex: none; }

  .tagline {
    position: absolute;
    bottom: 48px;
    left: 0;
    width: 100%;
    text-align: center;
    color: var(--white);
    font-size: 18px;
  }
</style>
</head>
<body>
  <section class="card card--back">
    <div class="back-pattern" role="img" aria-label="Repeating pattern of the brand mark fading from dark navy to bright blue"></div>
  </section>

  <section class="card card--front">
    <div class="brand">
      <span class="brand__dot"></span>
      <span class="brand__name">Calmora Advisory Group</span>
    </div>
    <div class="brand__rule"></div>

    <div class="person">
      <p class="person__name">Dana Weltrup</p>
      <p class="person__role">Managing Director</p>
      <p class="person__role">Aerospace and Defence</p>
    </div>

    <div class="divider"></div>

    <ul class="contact">
      <li>
        <svg viewBox="0 0 24 24" fill="none" stroke="#2a9bc4" stroke-width="2.4"><path d="M5 3h4l2 5-3 2a12 12 0 0 0 6 6l2-3 5 2v4a2 2 0 0 1-2 2A18 18 0 0 1 3 5a2 2 0 0 1 2-2z"/></svg>
        514-268-3917
      </li>
      <li>
        <svg viewBox="0 0 24 24" fill="none" stroke="#2a9bc4" stroke-width="2.4"><rect x="3" y="5" width="18" height="14" rx="1"/><path d="M3 6l9 7 9-7"/></svg>
        dana.weltrup@calmora-example.com
      </li>
      <li>
        <svg viewBox="0 0 24 24" fill="none" stroke="#2a9bc4" stroke-width="2.4"><circle cx="12" cy="12" r="9"/><path d="M3 12h18M12 3c3 3 3 15 0 18M12 3c-3 3-3 15 0 18"/></svg>
        www.calmora-example.com
      </li>
    </ul>

    <p class="tagline">Proposals Management and Capture support for complex procurements</p>
  </section>
</body>
</html>
```